Need a new office flyer

I would like an 8.5 x 11" flyer made that can be emailed or printed out and handed to potential customers.  The flyer should include our existing logo and continuity of branding.   I am a commercial real estate broker and market myself to business with 5-50 employee's that are looking to buy or lease space to run their business from.  I focus my efforts on office & warehouse space. The flyer should have a banner "need a new location "
"VLD commercial real estate specializes in helping business and professionals buy/sell or lease  the best spaces for their business.  Take the stress & time out of finding the best location for your business and negotiating a great deal  VLD will do it for you and the best part our service is free to you. Working with VLD is easy as 1, 2, 3
1. Call, Text, Email us today and let us know what your looking to do.
2. VLD  will prepare a list of all the best available spaces that meet your specifications and set up tours of your favorites.
3. We will negotiate the best terms for your space. and help you with all the  details of getting your new space ready for you.
Don't forget the that our services are free to Buyers and Tenants so don't waste your companies time searching for locations, we already know where they are!
Contact us today!
Dale Norcutt
DRE 07354128
VLD Commercial Real Estate
555-317-4829
d.norcutt@vldprop-example.com

```html
<!DOCTYPE html>
<html lang="en">
<head>
<meta charset="utf-8">
<title>VLD Commercial Real Estate – Need a New Location</title>
<link href="https://fonts.googleapis.com/css2?family=Exo+2:wght@800&family=Montserrat:wght@300;400;500;600;700&display=swap" rel="stylesheet">
<style>
  :root {
    --brand-blue: #2c6fa6;
    --brand-blue-dark: #225b8a;
    --grey: #9a9a9a;
    --grey-light: #f0f0f0;
    --ink: #333333;
    --white: #ffffff;
  }
  * { box-sizing: border-box; margin: 0; padding: 0; }
  html, body { width: 902px; height: 1200px; overflow: hidden; background: var(--white); }
  body { font-family: "Montserrat", sans-serif; color: var(--ink); }
  .flyer { position: relative; width: 902px; height: 1200px; overflow: hidden; background: var(--white); }

  .brand { position: absolute; left: 46px; top: 64px; display: flex; align-items: center; gap: 14px; }
  .brand-dot { width: 96px; height: 96px; border-radius: 50%; background: var(--brand-blue); }
  .brand-name { font-weight: 700; font-size: 74px; line-height: 1; color: var(--brand-blue); letter-spacing: 2px; }
  .brand-tag { display: block; font-weight: 500; font-size: 13px; letter-spacing: 4.5px; color: var(--brand-blue); margin-top: 4px; }

  .headline-band { position: absolute; left: 0; top: 189px; width: 440px; height: 284px; background: var(--brand-blue); }
  .headline { position: absolute; left: 56px; top: 222px; font-family: "Exo 2", sans-serif; font-weight: 800; color: var(--white); line-height: 1; }
  .headline span { display: block; }
  .headline .l1 { font-size: 54px; letter-spacing: 2px; }
  .headline .l2 { font-size: 98px; letter-spacing: 3px; margin-top: 18px; }
  .headline .l3 { font-size: 45px; letter-spacing: 1.5px; margin-top: 20px; }

  .hero-rings { position: absolute; left: 0; top: 0; width: 902px; height: 620px; pointer-events: none; }
  .hero-photo { position: absolute; left: 478px; top: 112px; width: 420px; height: 420px; border-radius: 50%;
    background: radial-gradient(circle at 40% 20%, #dfe9f3 0%, #6f9cc8 30%, #2f5f92 60%, #1c2f47 100%); }

  .specialty-bar { position: absolute; left: 0; top: 499px; width: 540px; height: 84px; background: var(--grey);
    color: var(--white); font-weight: 600; font-size: 23px; line-height: 1.3; padding: 14px 0 0 58px; }

  .benefit { position: absolute; left: 58px; display: flex; gap: 18px; font-size: 16.5px; line-height: 1.3; color: var(--ink); }
  .benefit strong { font-weight: 600; }
  .benefit-icon { flex: none; width: 58px; height: 58px; border-radius: 50%; background: var(--grey); display: flex; align-items: center; justify-content: center; }
  .benefit-1 { top: 612px; width: 460px; }
  .benefit-2 { top: 697px; width: 460px; }

  .steps-panel { position: absolute; left: 0; top: 805px; width: 515px; height: 347px; background: var(--brand-blue);
    border-top-right-radius: 70px; border-bottom-right-radius: 28px; color: var(--white); padding: 32px 0 0 58px; }
  .steps-title { font-weight: 600; font-size: 19px; letter-spacing: .3px; margin-bottom: 20px; }
  .step { display: flex; align-items: center; gap: 16px; height: 90px; font-weight: 500; font-size: 13px; line-height: 1.4; }
  .step-badge { flex: none; position: relative; width: 78px; height: 58px; }
  .step-num { position: absolute; left: 0; top: -8px; font-size: 66px; font-weight: 700; line-height: 1; color: transparent; -webkit-text-stroke: 2px var(--white); }
  .step-ring { position: absolute; right: 0; top: 4px; width: 52px; height: 52px; border-radius: 50%; border: 2px solid var(--white); background: var(--brand-blue); display: flex; align-items: center; justify-content: center; }
  .step-ring i { display: block; width: 30px; height: 30px; border-radius: 50%; background: var(--white); }
  .step p { width: 330px; }

  .services-panel { position: absolute; left: 541px; top: 640px; width: 361px; height: 519px;
    background: linear-gradient(90deg, var(--grey-light), var(--white) 40%); }
  .reminder { position: absolute; left: 565px; top: 660px; font-weight: 300; line-height: 1.2; color: var(--ink); }
  .reminder .r1 { display: block; font-size: 24px; }
  .reminder .r2 { display: block; font-size: 30px; margin-top: 4px; }

  .free-box { position: absolute; left: 541px; top: 755px; width: 321px; height: 80px; background: var(--brand-blue); color: var(--white);
    display: flex; align-items: center; padding-left: 22px; gap: 8px; }
  .free-box .big { font-weight: 700; font-size: 58px; letter-spacing: -1px; }
  .free-box .small { font-weight: 400; font-size: 21px; line-height: 1.1; }
  .free-note { position: absolute; left: 565px; top: 846px; width: 300px; font-size: 16.5px; line-height: 1.3; }

  .contact-bar { position: absolute; left: 541px; top: 936px; width: 323px; height: 50px; background: var(--brand-blue); color: var(--white);
    font-weight: 600; font-size: 25px; display: flex; align-items: center; padding-left: 24px; }
  .agent { position: absolute; left: 572px; top: 1002px; line-height: 1.35; }
  .agent-name { font-weight: 700; font-size: 19px; letter-spacing: .5px; }
  .agent-license { font-size: 15px; color: #555; }
  .agent-company { font-weight: 600; font-size: 16.5px; }
  .agent-line { display: flex; align-items: center; gap: 10px; margin-top: 6px; }
  .agent-phone { font-weight: 700; font-size: 26px; }
  .agent-email { font-weight: 600; font-size: 16px; margin-top: 0; }

  .footer-band { position: absolute; left: 0; bottom: 0; width: 902px; height: 41px; background: var(--grey); }
</style>
</head>
<body>
<main class="flyer">

  <div class="brand">
    <div class="brand-dot"></div>
    <div>
      <div class="brand-name">VLD</div>
      <span class="brand-tag">COMMERCIAL REAL ESTATE</span>
    </div>
  </div>

  <div class="headline-band"></div>
  <h1 class="headline"><span class="l1">NEED A</span><span class="l2">NEW</span><span class="l3">LOCATION</span></h1>

  <svg class="hero-rings" viewBox="0 0 902 620" aria-hidden="true">
    <circle cx="688" cy="322" r="262" fill="var(--white)"/>
    <path d="M 560 95 A 252 252 0 1 0 900 480" fill="none" stroke="var(--brand-blue)" stroke-width="22"/>
    <path d="M 720 74 A 250 250 0 0 1 902 500" fill="none" stroke="var(--brand-blue)" stroke-width="10"/>
    <circle cx="688" cy="322" r="226" fill="none" stroke="var(--grey)" stroke-width="14"/>
  </svg>
  <div class="hero-photo" role="img" aria-label="Upward view of glass office towers against a blue sky with clouds"></div>

  <div class="specialty-bar">VLD COMMERCIAL REAL ESTATE<br>SPECIALIZES IN</div>

  <div class="benefit benefit-1">
    <div class="benefit-icon">
      <svg width="30" height="30" viewBox="0 0 30 30" aria-hidden="true"><rect x="5" y="4" width="12" height="23" fill="#fff"/><rect x="18" y="11" width="8" height="16" fill="#fff"/><g fill="#9a9a9a"><rect x="8" y="8" width="2" height="2"/><rect x="12" y="8" width="2" height="2"/><rect x="8" y="13" width="2" height="2"/><rect x="12" y="13" width="2" height="2"/><rect x="8" y="18" width="2" height="2"/><rect x="12" y="18" width="2" height="2"/></g></svg>
    </div>
    <p>Helping business and professionals <strong>buy/sell or lease</strong> the best spaces for their business.</p>
  </div>

  <div class="benefit benefit-2">
    <div class="benefit-icon">
      <svg width="32" height="32" viewBox="0 0 32 32" aria-hidden="true"><circle cx="16" cy="8" r="5" fill="#fff"/><circle cx="8" cy="18" r="4" fill="#fff"/><circle cx="24" cy="18" r="4" fill="#fff"/><path d="M2 30 q6 -9 12 0z M18 30 q6 -9 12 0z" fill="#fff"/></svg>
    </div>
    <p>Take the stress &amp; time out of finding the <strong>best location</strong> for your business and <strong>negotiating a great deal</strong> VLD will do it for you and the best part our service is free to you.</p>
  </div>

  <section class="steps-panel">
    <h2 class="steps-title">WORKING WITH VLD IS EASY AS 1, 2, 3</h2>
    <div class="step">
      <div class="step-badge"><span class="step-num">1</span><span class="step-ring"><i></i></span></div>
      <p>Call, Text, Email us today and let us know what your looking to do.</p>
    </div>
    <div class="step">
      <div class="step-badge"><span class="step-num">2</span><span class="step-ring"><i></i></span></div>
      <p>VLD will prepare a list of all the best available spaces that meet your specifications and set up tours of your favorites.</p>
    </div>
    <div class="step">
      <div class="step-badge"><span class="step-num">3</span><span class="step-ring"><i></i></span></div>
      <p>We will negotiate the best terms for your space. and help you with all the details of getting your new space ready for you.</p>
    </div>
  </section>

  <div class="services-panel"></div>
  <p class="reminder"><span class="r1">DON'T FORGET THE THAT</span><span class="r2">OUR SERVICES ARE</span></p>
  <div class="free-box"><span class="big">FREE</span><span class="small">TO BUYERS<br>AND TENANTS</span></div>
  <p class="free-note">so don't waste your companies time searching for locations, we already know where they are!</p>

  <div class="contact-bar">CONTACT US TODAY!</div>
  <address class="agent" style="font-style:normal">
    <div class="agent-name">DALE NORCUTT</div>
    <div class="agent-license">DRE 07354128</div>
    <div class="agent-company">VLD Commercial Real Estate</div>
    <div class="agent-line">
      <svg width="18" height="18" viewBox="0 0 24 24" aria-hidden="true"><circle cx="12" cy="12" r="10.5" fill="none" stroke="var(--brand-blue)" stroke-width="2"/><path d="M8 6.5 l2 -0.5 1.2 3 -1.4 1.2 q1 2.4 3.4 3.6 l1.2 -1.4 3 1.2 -0.5 2 q-5 1 -8.9 -9.1z" fill="var(--brand-blue)"/></svg>
      <span class="agent-phone">555-317-4829</span>
    </div>
    <div class="agent-line">
      <svg width="16" height="12" viewBox="0 0 16 12" aria-hidden="true"><rect width="16" height="12" fill="var(--brand-blue)"/><path d="M0 0 L8 7 L16 0" fill="none" stroke="#fff" stroke-width="1.5"/></svg>
      <span class="agent-email">d.norcutt@vldprop-example.com</span>
    </div>
  </address>

  <div class="footer-band"></div>
</main>
</body>
</html>
```